Bright Leaf Company Needs New Packaging Design

We need a design to print directly on our stand up zip pouches, 6x9x3 in., to replace the labels we were applying on generic matte black pouches.

We'd like to keep the current color theme of matte black + [Flavor Color] (in this case, fushia) to communicate the idea of modern, luxury brand (please see velcorra coffee brand) and stay somewhat close to the current label so our product will be recognized by actual customers. Other flavors will be a declination of the same layout, matte black + [flavor color]. Colors used should be vibrant, eye catching, to stand out from competition.

We also want to display the actual tea blend picture on the packaging so the consumer can see how beautiful the tea is. The font size for Amber Orchard Meadow should be big enough so it's readable when the product is seen in thumbnail format.

The front should have a seal/stamp close to a top corner with a big "100% Freshness Guarantee",

The company logo "The Lumo Company" should be present on the front in a prominent spot. It's provided in the zip file from old label.

We need to display the net weight (4oz / 113g) and number of servings (makes 60 cups). Please refer to old label.

On the back side we need a space for the UPC barcode at the bottom, the company address, a space for the brand's story/mission, steeping instructions with icons (see current label), ingredients and another section featuring our other products. All fonts should be 10pt or bigger.

Artwork of the current label current label is available here
https://files.zentrovault.example/folders/7Qx2mRpL4vNa8sKd1TyHwBcE?resourcekey=0-Fk39LwQpz8RnVt2XyMbCaJ&usp=sharing

Target Market(s)

USA market, Women ages 25-45, young & young at heart, trendy, health conscious, luxury

Industry/Entity Type

Premium Loose Leaf Tea

Font styles to use
Other font styles liked:
• fonts provided in zip file

Colors
E54698
E96AAD
F1A4CE
F9D9EA
FCEFF6

Requirements
Must have
• See description
Should not have
• Asian look and feel

```html
<!DOCTYPE html>
<html lang="en">
<head>
<meta charset="utf-8">
<title>Amber Orchard Meadow Tea – Pouch Front</title>
<link href="https://fonts.googleapis.com/css2?family=Roboto+Condensed:wght@400;700&family=Lobster&display=swap" rel="stylesheet">
<style>
  :root {
    --backdrop: #ececec;
    --matte-black: #0b0a0b;
    --flavor: #e54698;
    --flavor-mid: #e96aad;
    --flavor-soft: #f1a4ce;
    --flavor-pale: #f9d9ea;
    --flavor-mist: #fceff6;
    --flavor-deep: #b13d86;
    --plum-ring: #8a2a6c;
    --title-pink: #dc63a9;
    --seal-green: #5cbc4f;
    --white: #ffffff;
    --blend-gold: #d9c23a;
    --blend-rose: #a8284e;
  }
  html, body {
    margin: 0;
    padding: 0;
    width: 1200px;
    height: 1200px;
    overflow: hidden;
    background: var(--backdrop);
  }
  .canvas {
    position: relative;
    width: 1200px;
    height: 1200px;
  }
  .pouch-front {
    position: absolute;
    left: 250px;
    top: 76px;
    width: 700px;
    height: 1048px;
  }
  .product-title {
    font-family: "Roboto Condensed", Arial, sans-serif;
    font-weight: 700;
    font-size: 86px;
    fill: var(--title-pink);
  }
  .brand-name {
    font-family: "Roboto Condensed", Arial, sans-serif;
    font-weight: 700;
    fill: var(--white);
  }
  .seal-text {
    font-family: "Roboto Condensed", Arial, sans-serif;
    font-weight: 700;
    fill: var(--white);
  }
  .seal-script {
    font-family: "Lobster", cursive;
    font-weight: 400;
    fill: var(--white);
  }
  .servings-text {
    font-family: "Roboto Condensed", Arial, sans-serif;
    font-weight: 700;
    fill: var(--matte-black);
  }
  .net-weight {
    font-family: "Roboto Condensed", Arial, sans-serif;
    font-size: 40px;
    fill: var(--white);
  }
  .net-weight .value { font-weight: 700; }
</style>
</head>
<body>
<main class="canvas">
  <svg class="pouch-front" viewBox="0 0 1095 1640" xmlns="http://www.w3.org/2000/svg">
    <defs>
      <linearGradient id="side-strip" x1="0" y1="0" x2="0" y2="1">
        <stop offset="0" stop-color="var(--flavor-soft)"/>
        <stop offset="0.55" stop-color="var(--flavor-pale)"/>
        <stop offset="1" stop-color="var(--white)"/>
      </linearGradient>
      <linearGradient id="flavor-band" x1="0" y1="0" x2="1" y2="0">
        <stop offset="0" stop-color="var(--flavor-deep)"/>
        <stop offset="0.45" stop-color="var(--flavor)"/>
        <stop offset="0.8" stop-color="var(--flavor-mid)"/>
        <stop offset="1" stop-color="var(--flavor-pale)"/>
      </linearGradient>
      <linearGradient id="bottom-line" x1="0" y1="0" x2="1" y2="0">
        <stop offset="0" stop-color="var(--flavor-deep)"/>
        <stop offset="0.7" stop-color="var(--flavor)"/>
        <stop offset="1" stop-color="var(--flavor-pale)"/>
      </linearGradient>
      <radialGradient id="blend-tones" cx="0.5" cy="0.45" r="0.6">
        <stop offset="0" stop-color="var(--blend-gold)"/>
        <stop offset="0.55" stop-color="#c9a43a"/>
        <stop offset="1" stop-color="var(--blend-rose)" stop-opacity="0.85"/>
      </radialGradient>
    </defs>

    <!-- pouch base -->
    <rect class="pouch-base" x="0" y="0" width="1095" height="1640" fill="var(--white)"/>

    <!-- right flavor strip -->
    <rect class="flavor-strip" x="930" y="0" width="165" height="1330" fill="url(#side-strip)"/>

    <!-- top matte black panel -->
    <path class="black-panel" d="M0,0 H945 V560 Q945,640 870,670 Q640,760 420,768 L0,768 Z" fill="var(--matte-black)"/>

    <!-- flavor swoosh band -->
    <path class="flavor-band" d="M0,768 L420,768 Q640,760 870,670 Q930,648 1095,640 L1095,820 Q930,826 760,855 Q420,905 0,900 Z" fill="url(#flavor-band)"/>

    <!-- tea blend photo area -->
    <g class="blend-photo" role="img" aria-label="Loose dried tea blend of chamomile buds, rose petals and lavender scattered on white">
      <path d="M30,920 Q240,880 520,890 Q820,860 960,860 Q990,980 940,1100 Q880,1180 760,1230 Q620,1340 520,1380 Q380,1350 260,1330 Q120,1300 60,1200 Q20,1080 30,920 Z" fill="url(#blend-tones)" opacity="0.9"/>
    </g>

    <!-- bottom accent line and black base -->
    <path class="bottom-accent" d="M50,1385 Q500,1350 1030,1290 L1095,1280 L1095,1300 L1030,1310 Q500,1370 50,1405 Z" fill="url(#bottom-line)"/>
    <path class="black-base" d="M50,1405 Q500,1370 1030,1310 L1095,1300 V1640 H0 V1405 Z" fill="var(--matte-black)"/>

    <!-- product title -->
    <text class="product-title" text-anchor="middle" x="425" y="410">Amber Orchard</text>
    <text class="product-title" text-anchor="middle" x="425" y="490">Meadow Tea</text>

    <!-- freshness seal -->
    <g class="freshness-seal">
      <circle cx="895" cy="328" r="98" fill="var(--seal-green)"/>
      <circle cx="895" cy="328" r="98" fill="none" stroke="var(--seal-green)" stroke-width="18" stroke-linecap="round" stroke-dasharray="0 25.6"/>
      <text class="seal-text" text-anchor="middle" x="905" y="280" font-size="32">100%</text>
      <text class="seal-script" text-anchor="middle" x="895" y="343" font-size="64">Fresh</text>
      <text class="seal-text" text-anchor="middle" x="895" y="385" font-size="32">Guarantee</text>
    </g>

    <!-- company name -->
    <g class="brand-lockup">
      <circle cx="345" cy="570" r="12" fill="var(--flavor-mid)"/>
      <text class="brand-name" text-anchor="middle" x="280" y="592" font-size="38">The</text>
      <text class="brand-name" text-anchor="middle" x="330" y="690" font-size="110">Lumo</text>
      <text class="brand-name" text-anchor="middle" x="330" y="745" font-size="44">Company</text>
    </g>

    <!-- servings badge -->
    <g class="servings-badge">
      <circle cx="330" cy="1490" r="92" fill="var(--white)"/>
      <path d="M405,1438 A92,92 0 1 0 420,1470" fill="none" stroke="var(--plum-ring)" stroke-width="16"/>
      <text class="servings-text" text-anchor="middle" x="335" y="1480" font-size="60">60</text>
      <text class="servings-text" text-anchor="middle" x="335" y="1536" font-size="56">Cups</text>
    </g>

    <!-- net weight -->
    <text class="net-weight" x="675" y="1545" transform="rotate(-4 675 1545)">Net Weigh <tspan class="value">4oz. 113 g</tspan></text>
  </svg>
</main>
</body>
</html>
```